Design Brief for Website Redesign

Client Name: Velmora IT
Website: www.velmorait.com.au
Industry: Managed IT Services
Target Audience: Small to medium-sized businesses in Australia, requiring IT solutions, IT support, cloud services, and phone systems.

Project Overview
We are seeking a full redesign of the Velmora IT website to modernize its look, improve usability, and enhance user experience across devices. The goal is to create a professional, clean, and user-friendly website that reflects our expertise in IT services and appeals to our business clients.

Objectives
Modern Visual Identity: Create a fresh, modern design that aligns with Velmora IT's branding.

Improved User Experience: Simplify navigation, improve accessibility, and enhance mobile responsiveness.

Clear Calls to Action: Ensure CTAs are prominent and encourage user engagement.

Enhanced Trust & Credibility: Highlight testimonials, case studies, and industry credentials.

SEO Optimization: Ensure the site is optimized for search engines, including proper heading structures and metadata.
Design Style & Tone
Professional: Clean, modern, and polished to reflect our IT expertise.

Minimalist: Simple layouts, plenty of white space, and easy-to-read typography.

Tech-focused: Subtle tech-themed design elements that reinforce our brand as a leading IT service provider.

Colors: Use our existing brand colors, or propose a color scheme that complements the tech industry while maintaining a professional feel.

Typography: Clear, readable fonts that convey professionalism and trustworthiness.

Key Pages & Features
Home Page:

Hero section with a clear value proposition.

Highlight key services (IT support, cloud solutions, phone systems, etc.) with icons and brief descriptions.

Prominent CTAs (e.g., “Request a Quote,” “Book a Demo”).

Testimonials from satisfied clients.

Services Page:

Detailed breakdown of the services we offer (IT support, cloud services, phone systems, etc.).

Use of icons or illustrations to make the services visually engaging.

Clear CTAs to request quotes or book consultations.

About Us Page:

Information about our company history, mission, and team.

Highlight our certifications, partnerships, and industry expertise.

Case Studies/Testimonials Page:

Showcase client success stories and testimonials with visuals and brief case study summaries.

Include a trust-building section with logos of major clients or partners.

Contact Page:

Simple contact form for inquiries.

Integrated map with office location.

Social media links and phone number.

Blog/Resource Section:

Easy-to-navigate blog section for IT-related articles, tips, and industry news.

Clear categorization and tags for easy browsing.

Knowledge Base/Support Page:

Self-service area for clients to find articles, FAQs, and support guides.

Option to submit a support ticket.

Mobile Responsiveness:

Ensure the design is fully responsive, with no horizontal scrolling or misaligned content on mobile.

Functional Requirements
Fast Load Times: Optimize images, minimize unnecessary scripts, and ensure the site loads quickly on both desktop and mobile.

User-Friendly CMS: We need a CMS that is easy to update (preferably WordPress, but open to other suggestions).

SEO Best Practices: Structure the site with proper metadata, alt tags, and semantic HTML for better search engine optimization.

Security: Ensure the website follows security best practices (SSL, HTTPS).

Deliverables
Full website design (desktop and mobile versions).

Design mockups in Photoshop, Sketch, or Figma (whichever is preferred).

Working prototype (optional).

Final website files, including images and assets.

A style guide for ongoing consistency.

Industry/Entity Type

IT Managed Services

Number of Pages Required

3 page

Requirements
Must have
• EXCELLENT UX/UI

```html
<!DOCTYPE html>
<html lang="en">
<head>
<meta charset="utf-8">
<title>Velmora IT – Home</title>
<link href="https://fonts.googleapis.com/css2?family=Poppins:ital,wght@0,400;0,500;0,600;1,400&display=swap" rel="stylesheet">
<style>
:root{
  --red:#e8213e;
  --ink:#14121c;
  --navy:#12112a;
  --muted:#6d6d74;
  --line:#e6e6e8;
  --stage:#e2e2e3;
  --white:#ffffff;
  --quote:#d9d9db;
}
*{box-sizing:border-box;margin:0;padding:0}
html,body{width:1187px;height:1200px;overflow:hidden}
body{background:var(--stage);font-family:"Poppins",sans-serif;color:var(--ink);position:relative}
.page{position:absolute;left:414px;top:31px;width:577px;height:1832px;background:var(--white);transform:scale(.6212);transform-origin:0 0;overflow:hidden}
.abs{position:absolute}
.brand{font-weight:600;color:var(--red);letter-spacing:.5px}
/* nav */
.nav{height:44px}
.nav .brand{left:41px;top:8px;font-size:21px}
.nav ul{list-style:none;position:absolute;left:300px;top:16px;display:flex}
.nav li{font-size:6px;width:43px;text-align:center}
.nav li.active{color:var(--red)}
.btn{display:inline-block;background:var(--red);color:var(--white);font-size:6px;font-weight:500;border-radius:9px;text-align:center}
.nav .btn{left:488px;top:15px;width:52px;height:16px;line-height:16px}
.btn-outline{display:inline-block;border:1px solid var(--red);color:var(--red);font-size:6px;border-radius:8px;width:38px;height:15px;line-height:13px;text-align:center}
/* hero */
.hero{left:0;top:44px;width:577px;height:301px;overflow:hidden}
.hero-photo{position:absolute;inset:0;background:linear-gradient(100deg,#5a0d16 0%,#8e1e28 30%,#b0433c 50%,#7b6f8c 68%,#5d7fb0 82%,#c9a43e 100%)}
.hero-copy{position:absolute;left:41px;top:50px;color:var(--white)}
.hero h1{font-size:38px;font-weight:500;line-height:42px;letter-spacing:-.3px}
.hero h2{font-size:15px;font-weight:500;line-height:23px;margin-top:6px}
.hero p{font-size:6.4px;line-height:13px;margin-top:6px;width:230px}
.hero .btn{margin-top:8px;width:76px;height:16px;line-height:16px}
.hero-wave{position:absolute;left:0;bottom:0;width:577px;height:80px}
/* managed */
.blob{left:30px;top:402px;width:240px;height:240px}
.managed{left:290px;top:406px;width:220px}
.managed h2{font-size:14px;font-weight:500}
.managed .lead{font-size:6px;line-height:13.5px;color:var(--muted);margin-top:12px}
.check{margin-top:12px}
.check h3{font-size:8px;font-weight:500;display:flex;align-items:center;gap:9px}
.check p{font-size:6px;line-height:13px;color:var(--muted);margin:9px 0 0 20px;width:150px}
.managed .btn-outline{margin:20px 0 0 20px}
.divider{left:72px;top:694px;width:438px;height:1px;background:var(--line)}
/* services */
.eyebrow{color:var(--red);font-size:8px;font-weight:500;text-align:center}
.section-title{font-size:15px;font-weight:500;text-align:center}
.svc-head{left:0;width:577px;top:730px}
.svc-head .section-title{margin-top:7px}
.svc-map{left:0;top:790px;width:577px;height:110px}
.svc{position:absolute;width:120px;text-align:center}
.svc h3{font-size:8px;font-weight:500}
.svc p{font-size:6px;line-height:13px;color:var(--muted);margin-top:5px}
/* reviews */
.reviews-wave{left:0;top:914px;width:577px;height:34px}
.reviews{left:0;top:946px;width:577px;height:318px;background:var(--red);color:var(--white)}
.reviews .eyebrow{color:var(--white);margin-top:54px}
.reviews .section-title{margin-top:6px}
.card{position:absolute;top:122px;width:217px;height:113px;background:var(--white);color:var(--ink);padding:26px 22px;overflow:hidden}
.card h3{font-size:8px;font-weight:500}
.card .stars{font-size:8px;letter-spacing:1px;margin-top:2px}
.card p{font-size:6px;font-style:italic;line-height:13px;color:var(--muted);margin-top:10px;width:140px}
.card .quote{position:absolute;right:20px;top:6px;font-size:96px;line-height:.9;height:60px;color:var(--quote);font-weight:600;font-family:Georgia,serif}
.pager{position:absolute}
/* media */
.media-title{left:47px;top:1312px;font-size:15px;font-weight:500}
.media-arrows{left:487px;top:1315px}
.post{position:absolute;top:1356px;width:151px}
.post .thumb{height:87px}
.post h3{font-size:8px;font-weight:500;margin-top:19px;white-space:nowrap}
.post p{font-size:6px;line-height:13.5px;color:var(--muted);margin-top:8px}
.post .btn-outline{margin-top:6px}
/* footer */
.footer-wave{left:0;top:1583px;width:577px;height:30px}
.footer{left:0;top:1612px;width:577px;height:220px;background:var(--navy);color:var(--white)}
.footer .brand{position:absolute;left:48px;top:42px;font-size:20px;color:var(--white)}
.footer .about{position:absolute;left:48px;top:80px;font-size:5.6px;line-height:13px;width:200px}
.social{position:absolute;left:48px;top:120px;display:flex;gap:12px}
.social span{width:13px;height:13px;border:1.4px solid var(--white);border-radius:50%}
.footer h4{font-size:8px;font-weight:500}
.footer ul{list-style:none;margin-top:14px}
.footer li{font-size:5.6px;line-height:16px}
.footer .col-pages{position:absolute;left:342px;top:60px}
.footer .col-contact{position:absolute;left:446px;top:60px}
.footer address{font-style:normal;font-size:5.6px;line-height:11.5px;margin-top:14px}
</style>
</head>
<body>
<main class="page">

  <header class="nav">
    <span class="abs brand">Velmora</span>
    <ul>
      <li class="active">Home</li><li>About</li><li>Services</li><li>Reviews</li>
    </ul>
    <span class="abs btn">Contact</span>
  </header>

  <section class="abs hero">
    <div class="hero-photo" role="img" aria-label="Photo of two colleagues working together at a laptop, with a deep red overlay on the left"></div>
    <div class="hero-copy">
      <h1>We innovate<br>technology</h1>
      <h2>Technology Solutions for a<br>better business</h2>
      <p>Ensure business continuity and prevent the risks of cyber-attack with Velmora IT's trusted cyber security solutions.</p>
      <span class="btn">Request a Quote</span>
    </div>
    <svg class="hero-wave" viewBox="0 0 577 80" preserveAspectRatio="none"><path d="M0 80 L0 78 C70 62 140 50 230 50 C320 50 380 68 450 58 C510 50 545 36 577 28 L577 80 Z" fill="#fff"/></svg>
  </section>

  <svg class="abs blob" viewBox="0 0 240 240" role="img" aria-label="Photo of a smiling woman working on a laptop, framed in an organic shape">
    <defs><linearGradient id="blobFill" x1="0" y1="0" x2="1" y2="1"><stop offset="0" stop-color="#e9eef0"/><stop offset=".55" stop-color="#c9cfcc"/><stop offset="1" stop-color="#5f7a56"/></linearGradient></defs>
    <path d="M10 50 C25 15 80 0 120 5 C160 10 195 25 205 45 C210 60 200 80 210 120 C222 165 215 210 170 225 C120 240 60 235 25 210 C-5 188 0 165 15 140 C30 115 5 85 10 50 Z" fill="#e8213e"/>
    <path d="M22 58 C35 25 80 12 120 15 C160 18 190 30 200 52 C205 70 195 90 205 125 C215 170 205 215 160 228 C115 240 65 232 35 212 C10 195 12 170 25 145 C38 120 15 90 22 58 Z" fill="url(#blobFill)"/>
  </svg>

  <section class="abs managed">
    <h2>Managed IT Services</h2>
    <p class="lead">We're Velmora IT, a Managed IT Services in Sydney provider. We offer expert IT Solutions and Support for Small and Medium Businesses.</p>
    <div class="check">
      <h3><svg width="11" height="11" viewBox="0 0 11 11"><circle cx="5.5" cy="5.5" r="5.5" fill="#e8213e"/><path d="M3 5.6 L4.8 7.3 L8 3.9" stroke="#fff" stroke-width="1.3" fill="none"/></svg>Providing Cutting-Edge</h3>
      <p>We're Velmora IT, a Managed IT Services in Sydney provider.</p>
    </div>
    <div class="check" style="margin-top:20px">
      <h3><svg width="11" height="11" viewBox="0 0 11 11"><circle cx="5.5" cy="5.5" r="5.5" fill="#e8213e"/><path d="M3 5.6 L4.8 7.3 L8 3.9" stroke="#fff" stroke-width="1.3" fill="none"/></svg>IT Solutions to Mid-Market</h3>
      <p>We're Velmora IT, a Managed IT Services in Sydney provider.</p>
    </div>
    <span class="btn-outline">More</span>
  </section>

  <div class="abs divider"></div>

  <section class="abs svc-head">
    <p class="eyebrow">VASP &amp; OTC</p>
    <h2 class="section-title">Highlight key services</h2>
  </section>

  <section class="abs svc-map">
    <svg width="577" height="110" viewBox="0 0 577 110" style="position:absolute;left:0;top:0">
      <path d="M141 25 C200 25 215 90 270 92 M306 92 C360 90 378 25 428 23" stroke="#888" stroke-width=".7" stroke-dasharray="2 2" fill="none"/>
      <g stroke="#e8213e" stroke-width="1" fill="none">
        <circle cx="58" cy="45" r="6.5"/><path d="M61 45 H55 M57.5 42.5 L55 45 L57.5 47.5"/>
        <circle cx="513" cy="45" r="6.5"/><path d="M510 45 H516 M513.5 42.5 L516 45 L513.5 47.5"/>
      </g>
      <circle cx="124" cy="23" r="13" fill="#e8213e"/>
      <g stroke="#fff" stroke-width="1" fill="none"><rect x="119" y="18" width="10" height="7" rx="1"/><path d="M117 27.5 H131"/></g>
      <circle cx="288" cy="90" r="13" fill="#e8213e"/>
      <g stroke="#fff" stroke-width="1" fill="none"><circle cx="288" cy="90" r="2"/><circle cx="288" cy="90" r="5" stroke-dasharray="2 1.3"/></g>
      <circle cx="443" cy="23" r="13" fill="#e8213e"/>
      <g stroke="#fff" stroke-width="1" fill="none"><rect x="439.5" y="16.5" width="7" height="13" rx="1.3"/><path d="M442 27 H444"/></g>
    </svg>
    <div class="svc" style="left:228px;top:15px"><h3>Cloud Solutions</h3><p>We're Velmora IT, a Managed IT Services in Sydney provider.</p></div>
    <div class="svc" style="left:64px;top:56px"><h3>Reliable IT Support</h3><p>We're Velmora IT, a Managed IT Services in Sydney provider.</p></div>
    <div class="svc" style="left:383px;top:56px"><h3>Phone Systems</h3><p>We're Velmora IT, a Managed IT Services in Sydney provider.</p></div>
  </section>

  <svg class="abs reviews-wave" viewBox="0 0 577 34" preserveAspectRatio="none"><path d="M0 34 L0 28 C90 6 190 10 290 22 C390 32 470 12 577 0 L577 34 Z" fill="#e8213e"/></svg>
  <section class="abs reviews">
    <p class="eyebrow">Reviews</p>
    <h2 class="section-title">What People Say About Us</h2>
    <article class="card" style="left:66px">
      <span class="quote" aria-hidden="true">“</span>
      <h3>Name Here</h3><div class="stars">★★★★★</div>
      <p>Effortlessly Receive, Send, and Exhange Payments — Integrating</p>
    </article>
    <article class="card" style="left:294px">
      <span class="quote" aria-hidden="true">“</span>
      <h3>Name Here</h3><div class="stars">★★★★★</div>
      <p>Effortlessly Receive, Send, and Exhange Payments — Integrating</p>
    </article>
    <svg class="pager" style="left:272px;top:260px" width="34" height="14" viewBox="0 0 34 14"><g stroke="#fff" stroke-width="1" fill="none"><circle cx="7" cy="7" r="6.3"/><path d="M10 7 H4 M6.5 4.5 L4 7 L6.5 9.5"/><circle cx="25" cy="7" r="6.3"/><path d="M22 7 H28 M25.5 4.5 L28 7 L25.5 9.5"/></g></svg>
  </section>

  <h2 class="abs media-title">Media Center</h2>
  <svg class="abs media-arrows" width="34" height="14" viewBox="0 0 34 14"><g stroke="#e8213e" stroke-width="1" fill="none"><circle cx="7" cy="7" r="6.3"/><path d="M10 7 H4 M6.5 4.5 L4 7 L6.5 9.5"/><circle cx="25" cy="7" r="6.3"/><path d="M22 7 H28 M25.5 4.5 L28 7 L25.5 9.5"/></g></svg>

  <article class="post" style="left:49px">
    <div class="thumb" role="img" aria-label="Photo of IT team members working at laptops in a bright office" style="background:linear-gradient(135deg,#e4e8ec,#9aa3ae 60%,#3d4450)"></div>
    <h3>Where IT experts are available</h3>
    <p>Effortlessly Receive, Send, and<br>Exhange Payments — Integrating</p>
    <span class="btn-outline">More</span>
  </article>
  <article class="post" style="left:209px">
    <div class="thumb" role="img" aria-label="Photo of a man working on a laptop at a desk by bookshelves" style="background:linear-gradient(135deg,#2f3e52,#4f6a86 55%,#8a7b6a)"></div>
    <h3>Security solutions with firewalls</h3>
    <p>Effortlessly Receive, Send, and<br>Exhange Payments — Integrating</p>
    <span class="btn-outline">More</span>
  </article>
  <article class="post" style="left:370px">
    <div class="thumb" role="img" aria-label="Photo of a woman at a laptop giving a thumbs up in a light office" style="background:linear-gradient(135deg,#f0f2f4,#d6dbe0 55%,#b8c2cc)"></div>
    <h3>Implementation of technology</h3>
    <p>Effortlessly Receive, Send, and<br>Exhange Payments — Integrating</p>
    <span class="btn-outline">More</span>
  </article>

  <svg class="abs footer-wave" viewBox="0 0 577 30" preserveAspectRatio="none"><path d="M0 30 L0 22 C100 0 200 0 290 14 C380 28 470 8 577 0 L577 30 Z" fill="#12112a"/></svg>
  <footer class="abs footer">
    <span class="brand">Velmora</span>
    <p class="about">Backup and recovery solutions to keep your data safe and reduce downtime in the event of a disaster.</p>
    <div class="social" aria-label="Social links"><span></span><span></span><span></span></div>
    <div class="col-pages">
      <h4>Pages</h4>
      <ul><li>Home</li><li>About</li><li>Services</li><li>Reviews</li><li>Contact</li></ul>
    </div>
    <div class="col-contact">
      <h4>Contact Details</h4>
      <address>Address<br>48 Harbour Lane<br>Suite 4, Harbourton, Australia<br><br>(02) 5550 1482<br>Mon – Sat<br>7:30 AM – 5:30 PM</address>
    </div>
  </footer>

</main>
</body>
</html>
```